Wordpress Layout, Plug-in, Mash-up Overhaul

We have collection of vertical topic portals; in each portal, a post typically is an article which goes with a subject video, following are 5 reference sites:

http://www.tallymint.com/
http://www.ladycounsel.com/
http://www.sparkvista.tv/
http://www.dwellingview.com/
http://www.gallerhum.com/

We obtained most of our based WP theme from various premium WP template membership sites, subsequently re-organise, mash-up content to produce sites as above; however we start to be constraint as we get into a fixed pattern of laying out our contents and we seeking professional help to re-work this. these re-work can includes as follows.

1. proposal on creative re-placement of component / re-layout on the templates. Should also suggest different way for the advertising banner placement etc.

2. proposal on right and appropriate use of WP plugins (paid or free but have to be secured and reliable) to achieve more relevant add-on of content where necessary (rss, etc)

Objective:
We want to move away from our internal team design constraint and also moving alway from being stuck with certain stereo-type way of WP content site. However the proposed WP design should still be a portal-centric type vs blogging/product-centric.

Deliverables:
1. We don't need the actual cut template but a design mockup of the home page and relevant sub pages (.psd, jpg etc) for the proposed re-design. Based on the above 5 listed sites, the deliverable would be at least 10 pages of design layout work (considering home page and 1 sub pages for each domain; could be more if necessary)

2. The plugins reference where necessary

What's expected from your proposal for the bid:
We would like a mockup of a re-design from any pick from any of the above 5 domains

```html
<!DOCTYPE html>
<html lang="en">
<head>
<meta charset="utf-8">
<title>Tallymint – How To Manage Your Finances</title>
<link href="https://fonts.googleapis.com/css2?family=Open+Sans:wght@400;600;700&family=Arimo:wght@400;700&display=swap" rel="stylesheet">
<style>
:root{
  --ink:#222;
  --body:#555;
  --muted:#777;
  --brand:#2d6c91;
  --brand-dark:#245a7a;
  --link:#1f5f86;
  --heading-blue:#1c3f73;
  --accent:#f5a90f;
  --topbar:#333;
  --bottombar:#1e1e1e;
  --line:#d6d6d6;
  --white:#fff;
}
*{margin:0;padding:0;box-sizing:border-box}
html,body{width:742px;height:1200px;overflow:hidden;background:var(--white)}
body{position:relative;font-family:"Open Sans",Arial,sans-serif;color:var(--ink)}
.abs{position:absolute}
a{color:inherit;text-decoration:none}

.topbar{left:0;top:0;width:742px;height:16px;background:var(--topbar);font-size:6.5px;color:#ddd;line-height:16px;padding-left:118px}
.topbar span{margin:0 3px}

.masthead{left:0;top:16px;width:742px;height:66px;background:var(--brand)}
.logo{left:114px;top:18px;display:flex;align-items:center;gap:6px}
.logo-mark{width:20px;height:20px;background:var(--accent)}
.logo-name{color:var(--white);font-weight:700;font-size:17px;line-height:1}
.distributor{left:222px;top:8px;width:298px;height:48px;background:var(--white);display:flex;align-items:center;padding-left:9px;gap:10px}
.distributor small{font-size:8.5px;color:#333}
.distributor strong{font-size:17px;font-weight:400;line-height:.95;color:#222;letter-spacing:.5px}
.distributor strong em{display:block;font-style:normal;font-size:7px;letter-spacing:0}
.connect{left:530px;top:17px;color:var(--white);font-size:7.5px;font-weight:700}
.social{left:572px;top:34px;display:flex;gap:12px}
.social i{display:block;width:9px;height:9px;border-radius:50%;background:var(--white)}

.mainnav{left:0;top:82px;width:742px;height:22px;border-bottom:1px solid var(--line);font-size:7.5px;color:#444}
.mainnav a{position:absolute;top:0;line-height:22px}
.mainnav .home{left:113px;width:38px;background:var(--accent);color:var(--white);text-align:center}
.searchbtn{left:611px;top:85px;border-left:1px solid #999;padding-left:5px;height:16px}

.page-title{left:113px;top:122px;font-size:11px;font-weight:400}
.page-title b{font-weight:700}

.video{left:113px;top:150px;width:273px;height:176px;background:linear-gradient(#3a3a3a,#1d1d1d)}
.video .controls{position:absolute;left:0;bottom:0;width:100%;height:8px;background:#e5e5e5}
.video .play{position:absolute;left:124px;top:74px;width:24px;height:20px;background:rgba(0,0,0,.6)}

.article{font-family:Arimo,Arial,sans-serif;font-size:6px;line-height:9.6px;color:var(--body)}
.article h3{font-size:6.5px;color:var(--heading-blue);font-weight:700}
.intro{left:402px;top:148px;width:236px}
.intro h3{margin:9px 0 8px}
.intro p{margin-bottom:0}
.section{left:113px;width:525px}
.section h3{margin-bottom:9px}

.related-title{left:113px;top:556px;font-size:11px}
.related-title b{font-weight:700}
.related{left:113px;top:584px;font-family:Arimo,Arial,sans-serif;font-size:7.5px;color:#444}
.related li{list-style:none;height:25px}
.related li.on{color:var(--link);font-weight:700}

.archive-title{left:113px;top:687px;font-size:11px}
.archive-title b{font-weight:700}
.arrows{left:444px;top:690px;display:flex;gap:2px}
.arrows i{width:9px;height:9px;background:#333;border-radius:2px;display:block}
.archive-photo{left:113px;top:714px;width:340px;height:123px;background:linear-gradient(120deg,#b79d72,#e7e2d9 45%,#cfc9bd)}
.archive-list{left:462px;top:714px;width:168px;border:1px solid var(--line);font-size:7.5px;color:#444}
.archive-list li{list-style:none;height:24.8px;line-height:24px;padding-left:28px;border-top:1px solid var(--line);position:relative}
.archive-list li:first-child{border-top:0;color:var(--link);font-weight:600}
.archive-list li::before{content:"";position:absolute;left:9px;top:8px;width:9px;height:9px;background:#333;border-radius:1px}
.archive-list li:first-child::before{background:var(--brand)}

.widget-head{top:850px;height:24px;border:1px solid #ccc;font-size:10.5px;font-weight:700;line-height:22px;padding-left:7px}
.post-card{height:40px;border:1px solid #ccc;display:flex;align-items:center;gap:9px;padding-left:2px;font-size:7.5px;font-weight:600;color:#333}
.post-card .thumb{width:34px;height:34px}
.post-list{top:882px;width:167px;display:flex;flex-direction:column;gap:6px}
.categories{left:462px;top:884px;width:168px;height:128px;border:1px solid #ccc;font-size:7.5px;color:#444;padding:4px 0 0 7px}
.categories li{list-style:none;height:18px;line-height:18px;display:flex;align-items:center;gap:8px}

.footer{left:0;top:1026px;width:742px;height:140px;background:var(--brand)}
.footer h4{position:absolute;top:24px;font-size:7px;font-weight:700;color:var(--white)}
.fpage{left:122px;top:40px;font-size:6px;color:var(--white);width:65px}
.fpage li{list-style:none;height:13.6px;line-height:13px;border-bottom:1px solid rgba(255,255,255,.25);display:flex;gap:4px;align-items:center}
.flatest{left:251px;top:42px;font-size:6px;color:var(--white);width:110px}
.flatest div{display:flex;align-items:center;gap:8px;height:36px;border-bottom:1px solid rgba(255,255,255,.25);margin-bottom:4px}
.flatest .thumb{width:28px;height:24px;background:linear-gradient(#d8c09a,#b89668)}
.fselect{left:382px;top:44px;width:108px;height:18px;background:var(--white);font-size:6.5px;line-height:18px;padding-left:8px;color:#333}
.fsearch{left:382px;top:98px;width:108px;height:18px;background:var(--white)}
.fwelcome{left:511px;top:42px;width:111px;font-size:6px;line-height:7px;color:var(--white);text-align:justify}
.bottombar{left:0;top:1166px;width:742px;height:34px;background:var(--bottombar);color:#ccc;font-size:6px;line-height:34px;padding-left:113px}
</style>
</head>
<body>

<div class="abs topbar"><span>About us</span>|<span>Advertise with us</span>|<span>Contact us</span>|<span>Privacy Policy</span>|<span>Sitemap</span></div>

<header class="abs masthead">
  <div class="abs logo"><span class="logo-mark"></span><span class="logo-name">Tallymint</span></div>
  <div class="abs distributor"><small>Exclusively distributed in the UAE by</small><strong>MERIDIAN<em>GENERAL TRADING LLC</em></strong></div>
  <div class="abs connect">Connect with Tallymint</div>
  <div class="abs social"><i></i><i></i><i></i></div>
</header>

<nav class="abs mainnav">
  <a class="home">Home</a>
  <a style="left:162px">Financial Management</a>
  <a style="left:257px">Insurance</a>
  <a style="left:310px">Investing</a>
  <a style="left:360px">Loans</a>
  <a style="left:399px">Real Estate</a>
  <a style="left:455px">Retirement</a>
  <a style="left:512px">Tax</a>
</nav>
<svg class="abs searchbtn" width="18" height="16" viewBox="0 0 18 16"><circle cx="9" cy="7" r="4" fill="none" stroke="#2d6c91" stroke-width="1.6"/><line x1="12" y1="10" x2="15" y2="13" stroke="#2d6c91" stroke-width="1.8"/></svg>

<h1 class="abs page-title"><b>How To</b> Manage Your Finances</h1>

<div class="abs video" role="img" aria-label="Video still: chalkboard sketch of a pie chart labelled expenses, tax, profit, income and cash flow">
  <div class="play"><svg width="24" height="20"><polygon points="9,5 17,10 9,15" fill="#fff"/></svg></div>
  <div class="controls"></div>
</div>

<div class="abs article intro">
  <p>Is never too late for a person to begin to manage their finances. Many people go through their entire lives and they feel like they never have a very good hold of their money. They may even be people that make a decent amount of income, but since they never get their finances under control they may find themselves in debt and completely and totally underwater financially. That does not need to be the case, because there are many things that a person can do in order to minute manage their finances.</p>
  <h3>Get A Financial Advisor</h3>
  <p>This is the first thing that a person can do if they feel like their finances are completely and totally out-of-control. There are many people that work online, in banks, or in other financial institutions that are very highly qualified and trained to help people to get a better hold of their finances. These are people that are able to work with others and help them to establish and maintain a good budget. They can help the person to get out of debt and they can help a person to pay off all of their credit cards a lot faster. Getting a financial advisor is a great idea, because since this is their profession they know exactly how to work with every type of budget in order to help person to attain their financial goals.</p>
</div>

<div class="abs article section" style="top:344px">
  <h3>Establish A Budget</h3>
  <p>Establishing a budget is one of the simplest ways that a person can get their finances under control. A good budget basically projects the amount of money that a person is going to be making each month and compares that to the amount of money that they are going to need to spend. A budget should take into account all of the persons monthly expenses regardless of how small they may be. It is very important that a person establishes a good budget and they should stick with that budget. In this way they can find that their money begins to work for them instead of against them.</p>
</div>
<div class="abs article section" style="top:412px">
  <h3>Always Save Money</h3>
  <p>Saving is one of the simplest ways that a person can keep themselves out of financial ruin. Many people live their daily lives and they spend the money that they make as quickly as they make it. When a person is constantly spending their money and not setting any money aside, when any unforeseen occurrence comes up they will not have the money to cover those expenses. When a person finds themselves in desperate need of money but have no way to obtain that money, the first thing that they will go to is their credit cards. Once a person begins to use their credit cards as their scapegoats they will find himself plunging deeper and deeper into debt. Since that is the last thing that a financially secure person wants to have to do, it is important to set aside money not only for emergencies, but also for any future event.</p>
</div>
<div class="abs article section" style="top:490px">
  <h3>You Can Manage Your Finances</h3>
  <p>Many people think that their finances are completely out of their control and that they have no way to get them back in order. The truth is that any person can manage their finances all that it takes is a little bit of initiative and the desire to have your money under control. With time and effort, a person can find that their money is working for them and that they are soon on their way to a more happy and a more financially secure future.</p>
</div>

<h2 class="abs related-title"><b>Related</b> Posts</h2>
<ul class="abs related">
  <li class="on">How To Prepare A Personal Budget</li>
  <li>How To Create A Balance Sheet</li>
  <li>How To Protect Your Money</li>
  <li>How To Do Financial Planning</li>
</ul>

<h2 class="abs archive-title"><b>Financial</b> Management Archive</h2>
<div class="abs arrows"><i></i><i></i></div>
<div class="abs archive-photo" role="img" aria-label="Photo: person working through bills with a calculator and coins on a desk"></div>
<ul class="abs archive-list">
  <li>How To Prepare A Personal Budget</li>
  <li>How To Create A Balance Sheet</li>
  <li>How To Manage Your Finances</li>
  <li>How To Protect Your Money</li>
  <li>How To Do Financial Planning</li>
</ul>

<div class="abs widget-head" style="left:113px;width:167px">Popular Posts</div>
<div class="abs widget-head" style="left:286px;width:168px">Recent Posts</div>
<div class="abs widget-head" style="left:462px;width:168px">Categories</div>

<div class="abs post-list" style="left:113px">
  <div class="post-card"><div class="thumb" role="img" aria-label="Photo: banknotes in hand" style="background:linear-gradient(#e8d6b4,#c99a6a)"></div>Repaying A Loan</div>
  <div class="post-card"><div class="thumb" role="img" aria-label="Photo: green planning chart" style="background:linear-gradient(#cfe08a,#6f8f3a)"></div>How to Do Financial Planning</div>
  <div class="post-card"><div class="thumb" role="img" aria-label="Photo: padlock on cash" style="background:linear-gradient(#9aa88a,#4a5a3e)"></div>How to Protect Your Money</div>
</div>
<div class="abs post-list" style="left:286px">
  <div class="post-card"><div class="thumb" role="img" aria-label="Photo: chalkboard finance sketch" style="background:linear-gradient(#3b3b3b,#1d1d1d)"></div>How To Manage Your Finances</div>
  <div class="post-card"><div class="thumb" role="img" aria-label="Photo: balance sheet with pen" style="background:linear-gradient(135deg,#f2f2f2,#2c4e8a 60%,#c8332b)"></div>How To Create A Balance Sheet</div>
  <div class="post-card"><div class="thumb" role="img" aria-label="Photo: banknotes in hand" style="background:linear-gradient(#e8d6b4,#c99a6a)"></div>Repaying A Loan</div>
</div>
<ul class="abs categories">
  <li><svg width="8" height="7"><polyline points="1,4 3,6 7,1" fill="none" stroke="#f5a90f" stroke-width="1.6"/></svg>Financial Management</li>
  <li><svg width="8" height="7"><polyline points="1,4 3,6 7,1" fill="none" stroke="#f5a90f" stroke-width="1.6"/></svg>Insurance</li>
  <li><svg width="8" height="7"><polyline points="1,4 3,6 7,1" fill="none" stroke="#f5a90f" stroke-width="1.6"/></svg>Investing</li>
  <li><svg width="8" height="7"><polyline points="1,4 3,6 7,1" fill="none" stroke="#f5a90f" stroke-width="1.6"/></svg>Loans</li>
  <li><svg width="8" height="7"><polyline points="1,4 3,6 7,1" fill="none" stroke="#f5a90f" stroke-width="1.6"/></svg>Real Estate</li>
  <li><svg width="8" height="7"><polyline points="1,4 3,6 7,1" fill="none" stroke="#f5a90f" stroke-width="1.6"/></svg>Retirement</li>
  <li><svg width="8" height="7"><polyline points="1,4 3,6 7,1" fill="none" stroke="#f5a90f" stroke-width="1.6"/></svg>Tax</li>
</ul>

<footer class="abs footer">
  <h4 style="left:126px">PAGE</h4>
  <h4 style="left:251px">LATEST</h4>
  <h4 style="left:382px">NAVIGATION</h4>
  <h4 style="left:511px">WELCOME TO TALLYMINT</h4>
  <h4 style="left:382px;top:79px">SEARCH</h4>
  <ul class="abs fpage">
    <li><svg width="6" height="5"><polyline points="0,3 2,5 6,0" fill="none" stroke="#fff" stroke-width="1.2"/></svg>About us</li>
    <li><svg width="6" height="5"><polyline points="0,3 2,5 6,0" fill="none" stroke="#fff" stroke-width="1.2"/></svg>Advertise With us</li>
    <li><svg width="6" height="5"><polyline points="0,3 2,5 6,0" fill="none" stroke="#fff" stroke-width="1.2"/></svg>Contact us</li>
    <li><svg width="6" height="5"><polyline points="0,3 2,5 6,0" fill="none" stroke="#fff" stroke-width="1.2"/></svg>Privacy Policy</li>
    <li><svg width="6" height="5"><polyline points="0,3 2,5 6,0" fill="none" stroke="#fff" stroke-width="1.2"/></svg>Sitemap</li>
  </ul>
  <div class="abs flatest">
    <div><span class="thumb" role="img" aria-label="Photo: banknotes in hand"></span>Repaying A Loan</div>
    <div style="border:0"><span class="thumb" role="img" aria-label="Photo: banknotes in hand"></span>Repaying A Loan</div>
  </div>
  <div class="abs fselect">Select Category
    <svg style="position:absolute;right:5px;top:7px" width="6" height="4"><polygon points="0,0 6,0 3,4" fill="#333"/></svg></div>
  <div class="abs fsearch"><svg style="position:absolute;right:7px;top:4px" width="10" height="10"><circle cx="4" cy="4" r="3" fill="none" stroke="#2d6c91" stroke-width="1.4"/><line x1="6" y1="6" x2="9" y2="9" stroke="#2d6c91" stroke-width="1.6"/></svg></div>
  <p class="abs fwelcome">We are a news source for all things related to business and finance. Our aim is to connect global events to their economic ramifications, giving you the news you need to make the right decisions. In a world of global instability, having news coverage that is fast, thorough, and in-depth is an invaluable asset.</p>
</footer>

<div class="abs bottombar">© Copyright Tallymint 2014. All rights reserved.</div>

</body>
</html>
```